IT services company needs a business card designed

-2 sided business card.-Front is going to be the logo raised (3D floating effect) on a black background. Make the logos spider web shiny silver and keep the spider the same design. -Back needs to have the following information:Darrel Sotho, Managing Partner, Cell: 738-402-1954, Website: Plankhorn.com, Email: Darrel@Plankhorn.com
Target Market(s)
IT Services
Industry/Entity Type
It Company
Contact Information for Business Card
-2 sided business card.
-Front is going to be the logo raised (3D floating effect) on a black background. Make the logos spider web shiny silver and keep the spider the same design.
-Back needs to have the following information:
Darrel Sotho, Managing Partner, Cell: 738-402-1954, Website: Plankhorn.com, Email: Darrel@Plankhorn.com

```html
<!DOCTYPE html>
<html lang="en">
<head>
<meta charset="utf-8">
<title>Plankhorn Business Card</title>
<link rel="stylesheet" href="https://fonts.googleapis.com/css2?family=Exo+2:wght@400&family=Open+Sans:wght@400;600&display=swap">
<style>
  :root {
    --stage: #e9ecef;
    --card-dark: #34546d;
    --card-dark-light: #4d7088;
    --accent: #1ea3e6;
    --paper: #ffffff;
    --ink-light: #f2f6f9;
    --ink-dark: #1c2228;
    --art-blue: #8fcbee;
    --art-silver: #c9d3da;
  }
  * { box-sizing: border-box; margin: 0; padding: 0; }
  html, body { width: 1200px; height: 896px; overflow: hidden; }
  body {
    background: var(--stage);
    font-family: "Open Sans", Arial, sans-serif;
    position: relative;
  }
  .card {
    position: absolute;
    top: 298px;
    width: 520px;
    height: 300px;
    border-radius: 22px;
    overflow: hidden;
    background: linear-gradient(135deg, var(--card-dark) 0%, var(--card-dark-light) 55%, var(--card-dark) 100%);
    box-shadow: 0 10px 26px rgba(0,0,0,0.25);
  }
  .card--front { left: 40px; }
  .card--back { left: 640px; }

  .logo { position: absolute; display: flex; flex-direction: column; align-items: center; }
  .logo__art {
    width: 150px; height: 110px; border-radius: 50%;
    background: radial-gradient(circle at 50% 50%, var(--art-blue) 0%, var(--art-silver) 45%, rgba(201,211,218,0) 72%);
  }
  .logo__name {
    font-family: "Exo 2", Arial, sans-serif;
    font-weight: 400;
    font-size: 40px;
    letter-spacing: 3px;
    line-height: 1;
    margin-top: 8px;
  }
  .card--front .logo { left: 0; right: 0; top: 62px; }
  .card--front .logo__name { color: var(--paper); }

  .back__disc { position: absolute; left: 0; top: 0; }
  .card--back .logo { left: 262px; top: 44px; width: 240px; }
  .card--back .logo__art { width: 130px; height: 96px; }
  .card--back .logo__name { color: var(--ink-dark); font-size: 32px; }

  .contact { position: absolute; left: 30px; bottom: 24px; color: var(--ink-light); }
  .contact__name {
    color: var(--accent);
    font-size: 22px; letter-spacing: 2px; text-transform: uppercase; font-weight: 400;
  }
  .contact__title { font-size: 13px; margin-bottom: 14px; }
  .contact__address { font-size: 13px; line-height: 1.45; margin-bottom: 12px; }
  .contact__list { list-style: none; font-size: 13px; line-height: 1.5; }
  .contact__list li { display: flex; align-items: center; gap: 7px; }
  .contact__list svg { width: 11px; height: 11px; flex: none; }
  .contact__brand { color: var(--accent); }
</style>
</head>
<body>

<section class="card card--front" aria-label="Card front">
  <div class="logo">
    <div class="logo__art" role="img" aria-label="Spider and web emblem area"></div>
    <div class="logo__name">PLANKHORN</div>
  </div>
</section>

<section class="card card--back" aria-label="Card back">
  <svg class="back__disc" width="520" height="300" viewBox="0 0 520 300" aria-hidden="true">
    <circle cx="400" cy="95" r="168" fill="none" stroke="var(--accent)" stroke-width="6"/>
    <circle cx="408" cy="88" r="168" fill="var(--paper)"/>
  </svg>
  <div class="logo">
    <div class="logo__art" role="img" aria-label="Spider and web emblem area"></div>
    <div class="logo__name">PLANKHORN</div>
  </div>

  <div class="contact">
    <h1 class="contact__name">Darrel Sotho</h1>
    <p class="contact__title">Managing Partner</p>
    <p class="contact__address">2817 Larkspur Lane<br>Dayton, OH 45402</p>
    <ul class="contact__list">
      <li>
        <svg viewBox="0 0 12 12"><path d="M3 1 L5 3.5 L4 5 Q5 7 7 8 L8.5 7 L11 9 L9.5 11 Q5 11 1 3 Z" fill="var(--accent)"/></svg>
        738-402-1954
      </li>
      <li>
        <svg viewBox="0 0 12 12"><rect x="1" y="2.5" width="10" height="7" rx="1" fill="var(--accent)"/><path d="M1.5 3 L6 6.5 L10.5 3" fill="none" stroke="var(--card-dark)" stroke-width="1"/></svg>
        Darrel@Plankhorn.com
      </li>
      <li>
        <svg viewBox="0 0 12 12"><circle cx="6" cy="6" r="5" fill="none" stroke="var(--accent)" stroke-width="1.3"/><path d="M1 6 H11 M6 1 Q3 6 6 11 Q9 6 6 1" fill="none" stroke="var(--accent)" stroke-width="1"/></svg>
        <span>www.<span class="contact__brand">Plankhorn</span>.com</span>
      </li>
    </ul>
  </div>
</section>

</body>
</html>
```